Bridal show post card design

our company contracts hotels near airports and cruise ports. We sell hotel packages including one night stay at a hotel (before or after the trip) including parking while they are away and transfers to and from the airport or cruise port. we are marketing to the public for the first time (typically it's travel agents). Specifically doing a Bridal show. Below are the photos that will appear in our booth or on our banners etc. We would like a post card to reflect the stress of not booking a hotel with us ... instead they could start their honeymoon or vacation a day early, stay at the hotel and relax... avoiding the stress of getting to the airport or cruise port in time otherwise missing the boat or the flight. We would also like to include a $20 off savings on the post card.

```html
<!DOCTYPE html>
<html lang="en">
<head>
<meta charset="utf-8">
<title>Gateway Stay &amp; Park – Bridal Show Postcard</title>
<link rel="stylesheet" href="https://fonts.googleapis.com/css2?family=Roboto:wght@300;400;700;900&display=swap">
<style>
  :root{
    --navy:#2c3557;
    --green:#5b8a3c;
    --header-grey:#d6d6d6;
    --white:#ffffff;
    --canvas:#e6e6e6;
    --body-grey:#7a7a7a;
  }
  *{margin:0;padding:0;box-sizing:border-box}
  html,body{width:1200px;height:707px;overflow:hidden;background:var(--canvas)}
  body{font-family:'Roboto',Arial,sans-serif;color:var(--navy)}
  .sheet{position:relative;width:1200px;height:707px}
  .card{position:absolute;top:163px;width:570px;height:380px;background:var(--white);overflow:hidden;
    box-shadow:0 2px 8px rgba(0,0,0,.18)}
  .card--back{left:20px}
  .card--front{left:610px}

  /* shared brand block */
  .brand{display:flex;flex-direction:column;align-items:center}
  .brand-name{font-weight:700;font-size:25px;color:var(--navy);line-height:1;white-space:nowrap}
  .brand-rule{width:190px;height:2px;background:var(--navy);margin:6px 0 4px}
  .brand-sub{font-weight:700;font-size:12px;color:var(--navy);letter-spacing:.5px}
  .brand-phone{font-weight:700;font-size:10px;color:var(--green);margin-top:3px;letter-spacing:.5px}

  /* back side */
  .back-art{position:absolute;left:330px;top:18px;width:150px;height:62px;border-radius:6px;
    background:linear-gradient(90deg,#4fa04a 0%,#9fd2e8 50%,#3f79b8 100%)}
  .back-brand{position:absolute;left:22px;top:100px;width:250px}
  .feature-list{position:absolute;left:290px;top:100px;width:258px;list-style:none}
  .feature-bar{height:34px;margin-bottom:8px;background:var(--navy);color:var(--white);
    font-size:20px;font-weight:300;letter-spacing:4px;display:flex;align-items:center;justify-content:center}
  .back-copy{position:absolute;left:290px;top:278px;width:258px;font-size:11px;line-height:1.45;
    color:var(--body-grey);font-weight:400}
  .back-call{position:absolute;left:290px;top:342px;font-size:13px;font-weight:700;color:var(--green)}

  /* front side */
  .header{position:absolute;left:0;top:0;width:570px;height:92px;background:var(--header-grey);
    display:flex;align-items:center;justify-content:center}
  .photo-row{position:absolute;left:0;top:98px;width:570px;height:120px;display:flex;gap:5px}
  .photo{flex:1;height:100%}
  .photo--shuttle{background:linear-gradient(160deg,#3a3a3a 0%,#1c1c1c 55%,#c79a2a 100%)}
  .photo--paris{background:linear-gradient(180deg,#2d4b85 0%,#c9784a 60%,#2a1f1d 100%)}
  .photo--beach{background:linear-gradient(170deg,#d9c4a4 0%,#bfa27c 100%)}
  .photo--snow{background:linear-gradient(180deg,#3f7fc4 0%,#cfe0ee 55%,#f3f6f8 100%)}

  .benefit-band{position:absolute;left:0;top:218px;width:570px;height:92px;background:var(--green);
    display:flex;color:var(--white)}
  .benefit{flex:1;display:flex;flex-direction:column;align-items:center;justify-content:center;text-align:center}
  .benefit svg{width:32px;height:23px;margin-bottom:4px}
  .benefit-title{font-weight:400;font-size:13px;letter-spacing:.5px}
  .benefit-text{font-weight:300;font-size:9.5px;line-height:1.2;margin-top:2px;max-width:110px}

  .divider{position:absolute;left:0;top:310px;width:570px;height:4px;background:var(--navy)}
  .offer{position:absolute;left:0;top:314px;width:570px;height:58px;display:flex;align-items:center;padding-left:140px;gap:18px}
  .offer-amount{display:flex;flex-direction:column;line-height:.9;font-weight:900;color:var(--navy)}
  .offer-enjoy{font-size:14px}
  .offer-price{font-size:27px}
  .offer-text{font-size:13px;font-weight:400;color:var(--navy);line-height:1.15;text-transform:uppercase}
  .offer-text strong{font-weight:900}
  .offer-art{position:absolute;right:18px;top:4px;width:54px;height:50px;border-radius:4px;
    background:linear-gradient(180deg,#4fa04a 0%,#9fd2e8 55%,#3f79b8 100%)}
  .footer-band{position:absolute;left:0;bottom:0;width:570px;height:8px;background:var(--navy)}
</style>
</head>
<body>
<main class="sheet">

  <article class="card card--back">
    <div class="back-art" role="img" aria-label="Illustration of palm trees, a striped suitcase, a plane and a globe"></div>
    <div class="brand back-brand">
      <div class="brand-name">Gateway Stay &amp; Park</div>
      <div class="brand-rule"></div>
      <div class="brand-sub">Bluewater Getaways</div>
      <div class="brand-phone">800-555-0142</div>
    </div>
    <ul class="feature-list">
      <li class="feature-bar">PARK</li>
      <li class="feature-bar">RELAX</li>
      <li class="feature-bar">SHUTTLE</li>
      <li class="feature-bar">ENJOY</li>
    </ul>
    <p class="back-copy">You can add a few lines about your company here, sed ut perspiciandam aut velenes molorem quia dolor sit amet.</p>
    <p class="back-call">Call 800-555-0142</p>
  </article>

  <article class="card card--front">
    <header class="header">
      <div class="brand">
        <div class="brand-name">Gateway Stay &amp; Park</div>
        <div class="brand-rule"></div>
        <div class="brand-sub">Bluewater Getaways</div>
        <div class="brand-phone">800-555-0142</div>
      </div>
    </header>

    <section class="photo-row">
      <div class="photo photo--shuttle" role="img" aria-label="Photo of an illuminated airport shuttle sign"></div>
      <div class="photo photo--paris" role="img" aria-label="Photo of a couple in silhouette before the Eiffel Tower at sunset"></div>
      <div class="photo photo--beach" role="img" aria-label="Photo of the word Relax written in beach sand"></div>
      <div class="photo photo--snow" role="img" aria-label="Photo of travellers resting in deck chairs on a snowy mountain"></div>
    </section>

    <section class="benefit-band">
      <div class="benefit">
        <svg viewBox="0 0 56 40" fill="#fff"><path d="M8 26 L12 14 Q13 11 17 11 H39 Q43 11 44 14 L48 26 H52 V32 H4 V26 Z"/><circle cx="15" cy="33" r="5" fill="#5b8a3c" stroke="#fff" stroke-width="3"/><circle cx="41" cy="33" r="5" fill="#5b8a3c" stroke="#fff" stroke-width="3"/></svg>
        <div class="benefit-title">PARK</div>
        <div class="benefit-text">safely leave your car at the hotel</div>
      </div>
      <div class="benefit">
        <svg viewBox="0 0 56 40" fill="#fff"><rect x="4" y="8" width="5" height="28"/><rect x="9" y="22" width="44" height="8"/><rect x="48" y="30" width="5" height="6"/><rect x="12" y="14" width="12" height="7" rx="2"/><rect x="26" y="15" width="27" height="6" rx="2"/></svg>
        <div class="benefit-title">RELAX</div>
        <div class="benefit-text">start your vacation a night early</div>
      </div>
      <div class="benefit">
        <svg viewBox="0 0 56 40" fill="#fff"><path d="M2 18 L14 20 L20 8 H24 L21 21 L30 22 L33 17 H36 L35 23 L36 29 H33 L30 24 L21 25 L24 38 H20 L14 26 L2 28 Z"/><path d="M38 26 H55 L52 34 H41 Z"/><rect x="42" y="20" width="8" height="5"/></svg>
        <div class="benefit-title">SHUTTLE</div>
        <div class="benefit-text">quickly get to the cruise- or airport</div>
      </div>
      <div class="benefit">
        <svg viewBox="0 0 56 40" fill="#fff"><path d="M8 18 Q22 2 40 10 Z"/><rect x="23" y="10" width="2.5" height="24" transform="rotate(-20 24 22)"/><rect x="6" y="34" width="44" height="3"/></svg>
        <div class="benefit-title">ENJOY</div>
        <div class="benefit-text">have a worry-free vacation</div>
      </div>
    </section>

    <div class="divider"></div>

    <section class="offer">
      <div class="offer-amount">
        <span class="offer-enjoy">ENJOY</span>
        <span class="offer-price">$20 OFF</span>
      </div>
      <p class="offer-text">One of our travel<br><strong>vacation packages</strong><br>with this postcard</p>
      <div class="offer-art" role="img" aria-label="Illustration of a striped suitcase beneath palm trees"></div>
    </section>

    <div class="footer-band"></div>
  </article>

</main>
</body>
</html>
```